Medical Device Packaging Project 2 of 5

We are a medical device startup company needing packaging for a total of 5 device brands. This is posting 2 of 5 and the device name is "Velmora"

Velmora is an intraocular lens for use in cataract surgery. The target market is Chinese ophthalmologists. The box should be sophisticated and upmarket.

The company name is Brindle Optics, I have included the logo in the uploaded files section. You should include the logo on the box.

I have uploaded a sample lens boxes from other companies that demonstrate the information needed to be contained on the box in terms of address, warnings, symbols, etc.

I have also uploaded the blank dieline of the boxes

You are welcome and encouraged to also submit to projects 1, 3, 4, and 5 as well. The same rules and expectations apply.

Requirements
Should not have
• Should not have any images of an eye or any bionic/futuristic feel to the design
• Note that the vantiscope box is for text reference only. You may use the lens image but the futuristic/bionic look is NOT what we are going for with this brand. It should be traditional upmarket medical device artwork.

```html
<!DOCTYPE html>
<html lang="en">
<head>
<meta charset="utf-8">
<title>Velmora – Carton Dieline</title>
<link rel="stylesheet" href="https://fonts.googleapis.com/css2?family=Montserrat:wght@400;500;600&family=Russo+One&family=Roboto+Condensed:wght@400&family=Noto+Sans+SC:wght@400&display=swap">
<style>
  :root{
    --page:#ffffff;
    --navy:#13305a;
    --navy-deep:#0f2a4f;
    --steel:#3f5b7c;
    --grey:#8d8f92;
    --ink-light:#eef2f6;
    --label:#333333;
  }
  *{margin:0;padding:0;box-sizing:border-box}
  html,body{width:800px;height:1200px;overflow:hidden;background:var(--page)}
  body{position:relative;font-family:"Montserrat",sans-serif;color:var(--ink-light)}
  .dieline{position:absolute;left:45px;top:194px;width:725px;height:812px}
  .dieline-art{position:absolute;left:0;top:0;width:725px;height:812px;overflow:visible}
  .dim{position:absolute;font-family:"Times New Roman",serif;font-size:12px;color:var(--label);white-space:nowrap}
  .dim--v{transform:rotate(-90deg);transform-origin:center}
  .abs{position:absolute}
  .brand{font-family:"Montserrat",sans-serif;font-weight:500;letter-spacing:.12em;line-height:1.15;color:var(--ink-light);white-space:nowrap;text-transform:uppercase;text-align:center}
  .product{font-family:"Russo One",sans-serif;letter-spacing:.06em;color:var(--ink-light);text-transform:uppercase;white-space:nowrap}
  .tagline{font-size:9px;letter-spacing:.03em;text-transform:uppercase;line-height:1.15;white-space:nowrap}

  .lid-address{position:absolute;left:380px;top:38px;width:166px;transform:rotate(180deg);font-size:8.5px;line-height:1.35;letter-spacing:.03em}

  .front-brand{left:420px;top:152px;width:136px;font-size:16px}
  .front-desc{left:420px;top:222px;width:136px;text-align:center;font-size:8px}
  .front-name{left:193px;top:343px;font-size:16px}
  .front-sub{left:193px;top:362px;font-size:9px}

  .side-left-brand{left:50px;top:326px;width:120px;font-size:13px;transform:rotate(90deg)}
  .side-right-brand{left:555px;top:170px;width:120px;font-size:13px;transform:rotate(-90deg)}

  .bottom-brand{left:176px;top:425px;width:96px;font-size:13px}
  .bottom-name{left:290px;top:416px;font-size:15px}
  .bottom-desc{left:290px;top:436px;font-size:8px}

  .back-name{left:177px;top:733px;font-size:13px}
  .back-sub{left:177px;top:749px;font-size:8px}

  .warnings{position:absolute;left:392px;top:506px;width:162px}
  .warning{border-left:1.5px solid var(--ink-light);padding-left:5px;margin-bottom:7px;font-family:"Roboto Condensed",sans-serif;font-size:6.5px;line-height:1.35;text-transform:uppercase;white-space:nowrap}
  .warning--zh{font-family:"Noto Sans SC",sans-serif;font-size:7.5px;letter-spacing:.18em;line-height:1.3}
</style>
</head>
<body>

<span class="dim" style="left:103px;top:172px">35mm</span>
<span class="dim" style="left:365px;top:176px">128mm</span>
<span class="dim" style="left:690px;top:172px">35mm</span>
<span class="dim" style="left:38px;top:290px">18mm</span>
<span class="dim" style="left:740px;top:290px">18mm</span>
<span class="dim dim--v" style="left:55px;top:246px">35mm</span>
<span class="dim dim--v" style="left:10px;top:438px">90mm</span>
<span class="dim dim--v" style="left:55px;top:634px">35mm</span>
<span class="dim dim--v" style="left:172px;top:820px">90mm</span>
<span class="dim dim--v" style="left:172px;top:986px">12mm</span>

<div class="dieline">
  <svg class="dieline-art" viewBox="0 0 725 812" xmlns="http://www.w3.org/2000/svg">
    <defs>
      <linearGradient id="bodyFade" gradientUnits="userSpaceOnUse" x1="100" y1="0" x2="600" y2="0">
        <stop offset="0" stop-color="#12305a"/>
        <stop offset=".35" stop-color="#3f5b7c"/>
        <stop offset=".72" stop-color="#8b9097"/>
        <stop offset="1" stop-color="#8e8f91"/>
      </linearGradient>
      <linearGradient id="sideRightFade" gradientUnits="userSpaceOnUse" x1="561" y1="0" x2="680" y2="0">
        <stop offset="0" stop-color="#8e8f91"/>
        <stop offset=".55" stop-color="#8a929c"/>
        <stop offset="1" stop-color="#13305a"/>
      </linearGradient>
      <radialGradient id="lensGlow" cx=".5" cy=".5" r=".5">
        <stop offset="0" stop-color="#c8d6e2" stop-opacity=".85"/>
        <stop offset=".6" stop-color="#a9bccd" stop-opacity=".55"/>
        <stop offset="1" stop-color="#a9bccd" stop-opacity="0"/>
      </radialGradient>
    </defs>

    <polygon class="flap" points="71,10 164,0 164,109 80,109 71,100" fill="var(--navy)"/>
    <rect class="lid-flap" x="164" y="0" width="397" height="109" fill="url(#bodyFade)"/>
    <polygon class="flap" points="561,0 654,10 654,100 645,109 561,109" fill="#8e8f91"/>

    <path class="tab" d="M12,112 H56 V385 H12 Q0,385 0,373 V124 Q0,112 12,112 Z" fill="var(--navy-deep)"/>
    <rect class="side-left" x="56" y="112" width="108" height="273" fill="var(--navy)"/>
    <rect class="front" x="164" y="109" width="397" height="279" fill="url(#bodyFade)"/>
    <rect class="side-right" x="561" y="112" width="109" height="273" fill="url(#sideRightFade)"/>
    <path class="tab" d="M670,112 H713 Q725,112 725,124 V373 Q725,385 713,385 H670 Z" fill="var(--navy)"/>

    <polygon class="flap" points="71,390 164,388 164,496 71,486" fill="var(--navy)"/>
    <rect class="bottom-flap" x="164" y="388" width="397" height="108" fill="url(#bodyFade)"/>
    <polygon class="flap" points="561,388 654,390 654,486 561,496" fill="#8e8f91"/>

    <rect class="back" x="164" y="496" width="397" height="279" fill="url(#bodyFade)"/>
    <rect class="tuck" x="164" y="775" width="397" height="37" fill="#8c8d8f"/>

    <g role="img" aria-label="Square grid pattern areas">
      <rect x="168" y="8" width="228" height="98" fill="#2d4f7a" opacity=".45"/>
      <rect x="60" y="118" width="100" height="140" fill="#2d4f7a" opacity=".45"/>
      <rect x="168" y="118" width="228" height="142" fill="#2d4f7a" opacity=".45"/>
      <rect x="398" y="256" width="160" height="128" fill="#76787c" opacity=".55"/>
      <rect x="565" y="256" width="58" height="128" fill="#7c7f84" opacity=".45"/>
      <rect x="398" y="394" width="160" height="98" fill="#76787c" opacity=".55"/>
      <rect x="168" y="500" width="228" height="78" fill="#2d4f7a" opacity=".45"/>
    </g>

    <ellipse role="img" aria-label="Intraocular lens with curved haptics" cx="381" cy="255" rx="100" ry="84" fill="url(#lensGlow)"/>
    <ellipse role="img" aria-label="Intraocular lens with curved haptics" cx="283" cy="668" rx="86" ry="68" fill="url(#lensGlow)"/>

    <g class="symbols-side" fill="none" stroke="#eef2f6" stroke-width="1">
      <circle cx="648" cy="268" r="5"/>
      <line x1="644.5" y1="264.5" x2="651.5" y2="271.5"/>
      <circle cx="648" cy="290" r="5"/>
      <line x1="644.5" y1="286.5" x2="651.5" y2="293.5"/>
      <circle cx="648" cy="313" r="5"/>
      <text x="648" y="316" text-anchor="middle" font-size="7" fill="#eef2f6" stroke="none" font-family="Montserrat,sans-serif" transform="rotate(-90 648 313)">2</text>
      <polygon points="648,330 654,341 642,341" transform="rotate(-90 648 336)"/>
      <rect x="642" y="350" width="12" height="30"/>
      <line x1="642" y1="369" x2="654" y2="369"/>
    </g>

    <g class="symbols-back" fill="none" stroke="#eef2f6" stroke-width="1">
      <rect x="382" y="745" width="42" height="18"/>
      <line x1="412" y1="745" x2="412" y2="763"/>
      <polygon points="440,744 451,764 429,764"/>
      <circle cx="467" cy="754" r="10"/>
      <circle cx="492" cy="754" r="10"/>
      <circle cx="517" cy="754" r="10"/>
      <line x1="510" y1="747" x2="524" y2="761"/>
    </g>
    <g font-family="Montserrat,sans-serif" fill="#eef2f6">
      <text x="384" y="757" font-size="6.5">STERILE</text>
      <text x="414" y="757" font-size="6.5" font-weight="600">EO</text>
      <text x="440" y="761" font-size="9" text-anchor="middle">!</text>
      <text x="467" y="758" font-size="11" text-anchor="middle">2</text>
      <text x="492" y="756" font-size="8" text-anchor="middle">2</text>
    </g>
  </svg>

  <div class="lid-address">
    BRINDLE OPTICS LIMITED<br>HONG KONG<br>www.brindleoptics.com
  </div>

  <div class="abs brand front-brand">Brindle<br>Optics</div>
  <div class="abs tagline front-desc">Hydrophobic Acrylic<br>Intraocular Lens</div>
  <div class="abs product front-name">Velmora</div>
  <div class="abs tagline front-sub">With 360° Square Edge</div>

  <div class="abs brand side-left-brand">Brindle<br>Optics</div>
  <div class="abs brand side-right-brand">Brindle<br>Optics</div>

  <div class="abs brand bottom-brand">Brindle<br>Optics</div>
  <div class="abs product bottom-name">Velmora</div>
  <div class="abs tagline bottom-desc">Hydrophobic Acrylic<br>Intraocular Lens<br>With 360° Square Edge</div>

  <div class="warnings">
    <p class="warning">Contains one sterile intraocular lens<br>Do not use if the package is damaged<br>Do not resterilize</p>
    <p class="warning warning--zh">内含无菌的眼内透镜一个<br>如果包装被损坏，请勿使用<br>请勿重新消毒</p>
    <p class="warning">Contient une sterile lentille intraoculaire<br>Ne pas utiliser si le forfait est endommagé<br>Ne pas restériliser</p>
    <p class="warning">Contiene uno sterile lente intraoculare<br>Non usare se il pacchetto è danneggiato<br>Non risterilizzare</p>
    <p class="warning">Enthält eine sterilische intraokulare Linse<br>Nicht verwenden, wenn das Paket schädigt wird<br>Nicht resterilieren</p>
    <p class="warning">Bevat één steriele intraoculaire lens<br>Niet gebruiken als de verpakking beschadigd is<br>Niet opnieuw steriliseren</p>
  </div>
  <div class="abs product back-name">Velmora</div>
  <div class="abs tagline back-sub">With 360° Square Edge</div>
</div>

</body>
</html>
```